Web Site Design for a Finance (lending) Company

We are opening a new subsidiary that focuses on lending money in the real estate industry. We need a web site designed to represent the business.

The business is lending money to real estate investors. A typical client/borrower will be looking to borrow money to buy a house, renovate it and then sell it at a profit, all within 12 months or less.

Company name is Varlo Finance. Our logo is attached.

Attached is a general outline for the web site. We're working on writing more text for each page but this should give you enough to get started with some ideas.

Competitor web site that I like a lot (as an example): https://brixhallfunding.example/. Many of the general items on this site match what we will need (description of loan programs, FAQ)

Target Market(s)

Real estate investors (generally individuals or small companies with just a few people) who are buying homes, renovating them and then selling them at a profit.

Industry/Entity Type

Finance

Coding

Coded - Design and coding required

Number of Pages Required

5+ page

Colors

Designer to choose colors to be used in the design.

Requirements
Must have
• Minimalist design. Clean lines without too much clutter. Some stock photography is ok but the photos should not be distracting. They should almost fade in to the background so that user can focus on the key information about what our company does instead. We are a finance company, not a design company, so the information about our products will be more interesting to site visitors than the art.
• Some minimalist examples from Mosaiko:
• https://www.mosaiko.example/explore/minimalist-web-design/
Nice to have
• If you search in searchly for "hard money lenders" you will find many examples of web sites from our competition. I have provided a link above to competitor web site that I like a lot.
• I have attached our logo in EPS format. Logo is green. Web site doesn't have to be green but it should be of a color that will work well with the logo.

```html
<!DOCTYPE html>
<html lang="en">
<head>
<meta charset="utf-8">
<title>Varlo Finance</title>
<link href="https://fonts.googleapis.com/css2?family=Roboto:wght@300;400;500;700&display=swap" rel="stylesheet">
<style>
:root{
  --green:#0f5a3a;
  --green-dark:#0b4a2f;
  --green-mid:#2f7656;
  --gray:#8c8c8c;
  --gray-light:#efefef;
  --gray-btn:#9a9a9a;
  --text:#333;
  --muted:#9a9a9a;
  --white:#fff;
}
*{box-sizing:border-box;margin:0;padding:0}
html,body{width:1200px;height:3340px;overflow:hidden}
body{position:relative;font-family:'Roboto',Arial,sans-serif;color:var(--text);background:var(--white)}
.abs{position:absolute}
.topbar{left:0;top:0;width:1200px;height:40px;background:var(--green);color:var(--white);font-size:14px}
.topbar .follow{left:78px;top:11px}
.soc{display:inline-block;width:24px;height:24px;border-radius:50%;background:rgba(255,255,255,.35);border:1px solid rgba(255,255,255,.6)}
.topbar .socials{left:166px;top:8px;display:flex;gap:8px}
.topbar .contact{right:78px;top:11px;display:flex;gap:36px;align-items:center}
.topbar .contact span{display:flex;align-items:center;gap:10px}
.header{left:0;top:40px;width:1200px;height:105px;background:var(--white)}
.nav{top:38px;display:flex;gap:8px;font-size:15px;text-transform:uppercase}
.nav a{color:#333;text-decoration:none;padding:12px 20px}
.nav a.active{background:var(--gray-btn);color:var(--white);border-radius:2px}
.brand{left:0;width:1200px;top:22px;text-align:center}
.brand-name{display:inline-flex;align-items:center;gap:14px;color:var(--green);font-size:36px;font-weight:500}
.brand-name i{display:inline-block;width:30px;height:30px;background:var(--green)}
.hero{left:0;top:145px;width:1200px;height:534px;background:linear-gradient(180deg,#3a3c40 0%,#5a5550 45%,#7a5e45 70%,#8f7a66 100%)}
.hero-arrow{z-index:5;width:40px;height:32px;background:var(--green);display:flex;align-items:center;justify-content:center}
.form{left:717px;top:338px;width:467px;height:474px;background:#e9e9e9;box-shadow:0 2px 8px rgba(0,0,0,.25)}
.form h3{height:67px;background:var(--green);color:var(--white);font-weight:400;font-size:24px;text-align:center;line-height:67px}
.field{position:absolute;left:18px;width:373px;height:44px;background:var(--white);border:1px solid #ddd;font-size:14px;color:#666;padding:0 14px;display:flex;align-items:center;justify-content:space-between}
.submit{position:absolute;left:111px;top:385px;width:167px;height:56px;background:var(--gray-btn);color:var(--white);font-size:22px;display:flex;align-items:center;justify-content:center}
.partners{left:0;top:679px;width:1200px;height:167px;background:var(--gray-light)}
.partner{top:58px;height:56px;display:flex;align-items:center;justify-content:center;text-align:center;white-space:nowrap;font-size:21px;font-weight:500;color:#444;line-height:22px}
.welcome{left:0;top:846px;width:1200px;height:396px;text-align:center}
.h2{font-size:40px;font-weight:500;color:var(--green);text-transform:uppercase}
.h2 span{color:var(--gray)}
.welcome .h2{margin-top:62px}
.welcome p{width:900px;margin:14px auto 0;font-size:13.5px;line-height:28px;color:var(--muted)}
.btn-gray{display:inline-flex;align-items:center;justify-content:center;background:var(--gray-btn);color:var(--white);font-weight:500;font-size:19px;text-transform:uppercase;border-radius:4px}
.loans{left:0;top:1242px;width:1200px;height:472px}
.loan-left{left:0;top:0;width:600px;height:472px;background:linear-gradient(160deg,#3c7c5e,#1f6345)}
.loan-right{left:600px;top:0;width:600px;height:472px;background:linear-gradient(200deg,#c8cdd3,#9aa4ad 60%,#b9b2a6)}
.loans h3{font-size:32px;font-weight:500;text-transform:uppercase;line-height:46px}
.loans p{font-size:13.5px;line-height:28px}
.loan-center{left:543px;top:160px;width:116px;height:116px;border-radius:50%;background:var(--white)}
.join{left:0;top:1714px;width:1200px;height:392px}
.join-photo{left:78px;top:16px;width:280px;height:313px;background:linear-gradient(180deg,#e6d7c9,#f4f4f4)}
.join-box{left:289px;top:100px;width:757px;height:229px;background:var(--green);border-radius:8px}
.join-box .frame{position:absolute;inset:8px;border:1px solid rgba(255,255,255,.5);border-radius:6px}
.join-box p{position:absolute;left:0;width:100%;top:50px;text-align:center;color:var(--white);font-size:19px;line-height:30px}
.jinput{position:absolute;top:127px;height:54px;width:230px;background:var(--white);font-size:14px;color:#555;padding:0 16px;display:flex;align-items:center}
.jbtn{position:absolute;left:552px;top:127px;width:187px;height:54px;border:2px solid var(--white);color:var(--white);font-size:20px;font-weight:500;display:flex;align-items:center;justify-content:center}
.testimonials{left:0;top:2106px;width:1200px;height:438px;background:linear-gradient(180deg,#2c6e50,#1f5e41);text-align:center;color:var(--white)}
.testimonials h2{margin-top:60px;font-size:40px;font-weight:400}
.testimonials h2 b{font-weight:700}
.client{top:160px;left:0;width:1200px;font-size:20px}
.client small{font-size:13px;color:rgba(255,255,255,.5);margin-left:22px}
.quote{left:151px;top:189px;width:895px;height:125px;border:1px solid rgba(255,255,255,.7);border-top:none;font-size:13.5px;line-height:26px;padding:22px 50px}
.quote:before{content:"";position:absolute;top:0;left:0;width:36%;border-top:1px solid rgba(255,255,255,.7)}
.quote:after{content:"";position:absolute;top:0;right:0;width:36%;border-top:1px solid rgba(255,255,255,.7)}
.qarrow{top:229px;width:41px;height:41px;background:var(--white);color:var(--green);display:flex;align-items:center;justify-content:center}
.dots{top:354px;left:0;width:1200px;display:flex;justify-content:center;gap:18px;align-items:center}
.dots i{width:10px;height:10px;border-radius:50%;background:var(--white)}
.dots i.on{width:16px;height:16px}
.team{left:0;top:2544px;width:1200px;height:454px}
.team .h2{position:absolute;left:0;width:1200px;top:60px;text-align:center}
.diamond{width:166px;height:166px;transform:rotate(45deg);border:4px solid #d9d9d9;background:linear-gradient(135deg,#c9cdd0,#8d9296)}
.dsoc{width:30px;height:30px;background:var(--green);border:2px solid var(--white);transform:rotate(45deg)}
.member h4{font-size:22px;font-weight:500;color:#222;text-transform:uppercase}
.member p{margin-top:14px;font-size:13.5px;line-height:27px;color:#666;width:270px}
.chat{left:1155px;top:2671px;width:45px;height:189px;background:var(--gray-btn);border-radius:6px 0 0 6px}
.chat span{position:absolute;left:0;top:20px;width:45px;height:110px;writing-mode:vertical-rl;transform:rotate(180deg);color:var(--white);font-size:16px;display:flex;align-items:center;justify-content:center;letter-spacing:1px}
.chat b{position:absolute;left:0;bottom:0;width:45px;height:45px;background:var(--green);border-radius:0 0 0 6px}
.footer{left:0;top:2998px;width:1200px;height:279px;background:var(--green);color:var(--white)}
.footer h5{font-size:17px;font-weight:500;text-transform:uppercase}
.footer ul{list-style:none;margin-top:26px}
.footer li{font-size:13.5px;line-height:34px;padding-left:26px;position:relative}
.footer li:before{content:"";position:absolute;left:4px;top:14px;width:7px;height:7px;background:rgba(255,255,255,.7)}
.fsoc{width:40px;height:40px;border-radius:50%;background:rgba(255,255,255,.2);border:2px solid rgba(255,255,255,.6)}
.citem{display:flex;gap:16px;font-size:14px;line-height:24px}
.copyright{left:0;top:3277px;width:1200px;height:63px;background:#9a9a9a;color:#333;font-size:14px;text-align:center;line-height:63px}
.copyright b{color:var(--green);font-weight:500}
</style>
</head>
<body>

<div class="abs topbar">
  <span class="abs follow">Follow Us :</span>
  <div class="abs socials"><i class="soc"></i><i class="soc"></i><i class="soc"></i></div>
  <div class="abs contact">
    <span><svg width="16" height="12" viewBox="0 0 16 12"><rect width="16" height="12" fill="#fff"/><path d="M0 0l8 6 8-6" stroke="#0f5a3a" stroke-width="1.5" fill="none"/></svg>info@varlofinance.example</span>
    <span><svg width="14" height="14" viewBox="0 0 24 24"><path fill="#fff" d="M6.6 10.8a15 15 0 0 0 6.6 6.6l2.2-2.2c.3-.3.7-.4 1-.2 1.1.4 2.3.6 3.6.6.6 0 1 .4 1 1V20c0 .6-.4 1-1 1A17 17 0 0 1 3 4c0-.6.4-1 1-1h3.5c.6 0 1 .4 1 1 0 1.3.2 2.5.6 3.6.1.3 0 .7-.2 1z"/></svg>123 456 7890</span>
  </div>
</div>

<header class="abs header">
  <nav class="abs nav" style="left:154px"><a class="active">Home</a><a>About Us</a><a>Loans</a></nav>
  <div class="abs brand"><span class="brand-name"><i></i>Varlo Finance</span></div>
  <nav class="abs nav" style="left:740px"><a>Resources</a><a>Contact Us</a>
    <a style="padding:10px 8px"><svg width="20" height="20" viewBox="0 0 20 20"><circle cx="8" cy="8" r="6" stroke="#0f5a3a" stroke-width="3" fill="none"/><path d="M12.5 12.5l6 6" stroke="#0f5a3a" stroke-width="3"/></svg></a></nav>
</header>

<section class="abs hero" role="img" aria-label="Businessman at a desk behind small model houses and stacks of coins"></section>

<section class="abs partners">
  <svg class="abs" style="left:78px;top:58px" width="18" height="50"><path d="M16 2L3 25l13 23" stroke="#bbb" stroke-width="2" fill="none"/></svg>
  <span class="abs partner" style="left:110px;width:170px">Tresor Finance</span>
  <span class="abs partner" style="left:292px;width:176px">Halden Finance</span>
  <span class="abs partner" style="left:482px;width:180px;font-size:19px;font-weight:500">Ostrava<br>Personal Finance</span>
  <svg class="abs" style="left:680px;top:58px" width="18" height="50"><path d="M2 2l13 23L2 48" stroke="#bbb" stroke-width="2" fill="none"/></svg>
</section>

<form class="abs form">
  <h3>CONTACT US</h3>
  <div class="field" style="top:87px">Name*<svg width="14" height="14" viewBox="0 0 14 14"><circle cx="7" cy="4" r="3.5" fill="#0f5a3a"/><path d="M0 14a7 6 0 0 1 14 0z" fill="#0f5a3a"/></svg></div>
  <div class="field" style="top:145px">Last Name*<svg width="14" height="14" viewBox="0 0 14 14"><circle cx="7" cy="4" r="3.5" fill="#0f5a3a"/><path d="M0 14a7 6 0 0 1 14 0z" fill="#0f5a3a"/></svg></div>
  <div class="field" style="top:203px">Phone*<svg width="14" height="14" viewBox="0 0 24 24"><path fill="#0f5a3a" d="M6.6 10.8a15 15 0 0 0 6.6 6.6l2.2-2.2c.3-.3.7-.4 1-.2 1.1.4 2.3.6 3.6.6.6 0 1 .4 1 1V20c0 .6-.4 1-1 1A17 17 0 0 1 3 4c0-.6.4-1 1-1h3.5c.6 0 1 .4 1 1 0 1.3.2 2.5.6 3.6.1.3 0 .7-.2 1z"/></svg></div>
  <div class="field" style="top:261px">Email*<svg width="15" height="11" viewBox="0 0 16 12"><rect width="16" height="12" fill="#0f5a3a"/><path d="M0 0l8 6 8-6" stroke="#fff" stroke-width="1.5" fill="none"/></svg></div>
  <div class="field" style="top:319px">How you heard about us *<svg width="14" height="8"><path d="M0 0h14L7 8z" fill="#0f5a3a"/></svg></div>
  <div class="submit">SUBMIT</div>
</form>

<div class="abs hero-arrow" style="left:0;top:428px"><svg width="10" height="14"><path d="M8 1L2 7l6 6" stroke="#fff" stroke-width="2" fill="none"/></svg></div>
<div class="abs hero-arrow" style="left:1160px;top:428px"><svg width="10" height="14"><path d="M2 1l6 6-6 6" stroke="#fff" stroke-width="2" fill="none"/></svg></div>

<section class="abs welcome">
  <h2 class="h2">Welcome to <span>Varlo Finance</span></h2>
  <p>Lorem Ipsum is simply dummy text of the printing and typesetting industry. Lorem Ipsum has been the industry's standard dummy text ever since the 1500s, when an unknown printer took a galley of type and scrambled.</p>
  <p style="margin-top:6px">Lorem Ipsum is simply dummy text of the printing and typesetting industry. Lorem Ipsum has been the industry's standard dummy text ever since the 1500s, when an unknown printer took a galley of type and scrambled it to make a type specimen book. It has survived not only five centuries, but also the leap into electronic typesetting, remaining essentially unchanged.</p>
  <span class="abs btn-gray" style="left:507px;top:278px;width:187px;height:56px">Know More</span>
</section>

<section class="abs loans">
  <div class="abs loan-left" role="img" aria-label="Two-storey house with porch under a green tint"></div>
  <div class="abs loan-right" role="img" aria-label="Office tower and hand holding keys under a pale tint"></div>
  <div class="abs" style="left:78px;top:86px;width:400px;color:#fff">
    <h3>Fix and Flip <span style="color:#b8cfc4">Loans</span></h3>
    <p style="margin-top:8px">Lorem Ipsum is simply dummy text of the printing and typesetting industry. Lorem Ipsum is simply.</p>
    <p style="margin-top:8px">Lorem Ipsum is simply dummy text of the printing and typesetting industry. Lorem Ipsum is simply dummy text of the printing and typesetting industry. Lorem Ipsum is simply dummy text of the printing.</p>
  </div>
  <span class="abs btn-gray" style="left:78px;top:323px;width:182px;height:56px">Know More</span>
  <div class="abs" style="left:722px;top:86px;width:402px;text-align:right;color:#fff">
    <h3 style="color:var(--green)">Commercial Hard<br><span style="color:#fff">Money Loan</span></h3>
    <p style="margin-top:12px">Lorem Ipsum is simply dummy text of the printing and typesetting industry. Lorem Ipsum is simply dummy text of the printing and typesetting industry. Lorem Ipsum is simply dummy text of the printing.</p>
  </div>
  <span class="abs btn-gray" style="left:940px;top:323px;width:182px;height:56px;background:transparent;border:2px solid #fff">Know More</span>
  <div class="abs loan-center"></div>
</section>

<section class="abs join">
  <div class="abs join-photo" role="img" aria-label="Smiling man in a white t-shirt holding a tablet"></div>
  <div class="abs join-box">
    <div class="frame"></div>
    <p>Varlo Finance is a local business with local knowledge and strong industry<br>relationships. A partner with a wide network who offers value added services.</p>
    <div class="jinput" style="left:78px">User Name *</div>
    <div class="jinput" style="left:316px">Enter Email *</div>
    <div class="jbtn">JOIN US</div>
  </div>
</section>

<section class="abs testimonials" role="img" aria-label="Grid of client portrait photos under a green tint">
  <h2>WHAT OUR <b>CLIENT SAY</b></h2>
  <div class="abs client">Client Name<small>something.com</small></div>
  <div class="abs quote">Lorem Ipsum is simply dummy text of the printing and typesetting industry. Lorem Ipsum has been the industry's standard dummy text ever since the 1500s, when an unknown printer took a galley of type and scrambled it to make a type specimen book. It has survived not only five centuries.</div>
  <div class="abs qarrow" style="left:122px"><svg width="10" height="14"><path d="M8 1L2 7l6 6" stroke="#0f5a3a" stroke-width="2" fill="none"/></svg></div>
  <div class="abs qarrow" style="left:1037px"><svg width="10" height="14"><path d="M2 1l6 6-6 6" stroke="#0f5a3a" stroke-width="2" fill="none"/></svg></div>
  <div class="abs dots"><i></i><i></i><i class="on"></i></div>
</section>

<section class="abs team">
  <h2 class="h2">Meet Our <span>Team</span></h2>
  <div class="abs diamond" style="left:113px;top:182px" role="img" aria-label="Portrait of a team member"></div>
  <div class="abs dsoc" style="left:280px;top:240px"></div>
  <div class="abs dsoc" style="left:255px;top:275px"></div>
  <div class="abs dsoc" style="left:230px;top:310px"></div>
  <div class="abs member" style="left:332px;top:170px"><h4>Member Name</h4><p>Lorem Ipsum is simply dummy text of the printing and typesetting industry. Lorem Ipsum has been the industry's standard dummy text ever since the 1500s, when an unknown printer took a galley of type and scrambled</p></div>
  <div class="abs diamond" style="left:652px;top:172px" role="img" aria-label="Portrait of a team member"></div>
  <div class="abs dsoc" style="left:680px;top:204px"></div>
  <div class="abs dsoc" style="left:652px;top:232px"></div>
  <div class="abs dsoc" style="left:625px;top:262px"></div>
  <div class="abs member" style="left:873px;top:170px"><h4>Member Name</h4><p>Lorem Ipsum is simply dummy text of the printing and typesetting industry. Lorem Ipsum has been the industry's standard dummy text ever since the 1500s, when an unknown printer took a galley of type..</p></div>
</section>

<div class="abs chat"><span>LIVE CHAT</span><b></b></div>

<footer class="abs footer">
  <div class="abs" style="left:78px;top:70px;color:#fff;font-size:32px;font-weight:500;display:flex;align-items:center;gap:12px"><i style="display:inline-block;width:26px;height:26px;background:#fff"></i>Varlo Finance</div>
  <div class="abs" style="left:112px;top:170px;display:flex;gap:12px"><i class="fsoc"></i><i class="fsoc"></i><i class="fsoc"></i></div>
  <div class="abs" style="left:338px;top:34px"><h5>Sitemap</h5>
    <ul><li>Home</li><li>About Us</li><li>Loans</li><li>Resources</li><li>Contact Us</li></ul></div>
  <div class="abs" style="left:599px;top:34px;width:250px"><h5>Contact Us</h5>
    <div class="citem" style="margin-top:22px"><svg width="16" height="22" viewBox="0 0 16 22"><path d="M8 0a8 8 0 0 1 8 8c0 6-8 14-8 14S0 14 0 8a8 8 0 0 1 8-8z" fill="#fff"/><circle cx="8" cy="8" r="3" fill="#0f5a3a"/></svg><div><b style="font-weight:500">VARLO FINANCE</b><br>Lorem Ipsum is simply dummy text of the printing and types</div></div>
    <div class="citem" style="margin-top:14px;font-size:16px"><svg width="18" height="18" viewBox="0 0 24 24"><path fill="#fff" d="M6.6 10.8a15 15 0 0 0 6.6 6.6l2.2-2.2c.3-.3.7-.4 1-.2 1.1.4 2.3.6 3.6.6.6 0 1 .4 1 1V20c0 .6-.4 1-1 1A17 17 0 0 1 3 4c0-.6.4-1 1-1h3.5c.6 0 1 .4 1 1 0 1.3.2 2.5.6 3.6.1.3 0 .7-.2 1z"/></svg>123 456 7890</div>
    <div class="citem" style="margin-top:18px"><svg width="18" height="13" viewBox="0 0 16 12"><rect width="16" height="12" fill="#fff"/><path d="M0 0l8 6 8-6" stroke="#0f5a3a" stroke-width="1.5" fill="none"/></svg>info@varlofinance.example</div>
  </div>
  <div class="abs" style="left:870px;top:34px;width:260px"><h5>Newsletter</h5>
    <p style="margin-top:16px;font-size:13.5px;line-height:26px">Would you like to receive exclusive access to articles, white papers and our regular monthly newsletter?</p>
    <div style="margin-top:12px;width:250px;height:45px;background:#fff;color:#555;font-size:13px;padding:0 12px;display:flex;align-items:center">Enter Email Id</div>
    <div style="margin-top:10px;width:187px;height:46px;border:2px solid #fff;font-size:19px;font-weight:500;display:flex;align-items:center;justify-content:center">SUBSCRIBE</div>
  </div>
</footer>

<div class="abs copyright">© <b>VARLO FINANCE</b> - 2017 All Right Reserved</div>

</body>
</html>
```